Corporate Two Sided Business Card

Looking for a Corporate "edgy" Modern look and feel for a business card

We are looking at two options. Dark background with our logo on it, white background with our logo on it - The background is more - Charcoal / Graphite then black

Details will be

Danielle Forsk

Licensee / Director

m. 0428 519 064

e. danielle@quorvela.com.au

quorvela.com.au

Target Market(s)

Professional Business people that refer use business and clients that own Investment Properties

Industry/Entity Type

Business

Contact Information for Business Card

Details will be

Danielle Forsk

Licensee / Director

m. 0428 519 064

quorvela.com.au

Font styles to use
Serif

Colors
000000
ec1f27
eeeeee
ffffff

Requirements
Must have
• Two options - White Background and Dark Background. - Two sided
Nice to have
• A design that is edgy, modern and new to look instead of boring style corporate cards - It should be a full integrated design
Should not have
• Block looking - Cheap.

```html
<!DOCTYPE html>
<html lang="en">
<head>
<meta charset="utf-8">
<title>Quorvela Business Card</title>
<link rel="stylesheet" href="https://fonts.googleapis.com/css2?family=Poppins:wght@500;600&family=Didact+Gothic&display=swap">
<style>
  :root {
    --charcoal: #2b2b2d;
    --red: #ec1f27;
    --card: #f4f4f4;
    --card-edge: #e6e6e6;
    --ink: #4a4a4c;
    --ink-soft: #5a5a5c;
    --white: #ffffff;
  }
  * { box-sizing: border-box; margin: 0; padding: 0; }
  html, body {
    width: 1200px; height: 834px; overflow: hidden;
    background: var(--charcoal);
  }
  .canvas {
    position: relative; width: 1200px; height: 834px;
    display: flex; align-items: center; justify-content: center; gap: 44px;
  }
  .card {
    position: relative; width: 540px; height: 330px;
    background: linear-gradient(135deg, var(--white) 0%, var(--card) 55%, var(--card-edge) 100%);
    box-shadow: 0 18px 40px rgba(0,0,0,.45);
    overflow: hidden;
  }
  .brand {
    display: flex; align-items: center; gap: 8px;
    font-family: "Poppins", sans-serif; font-weight: 500;
    color: var(--ink-soft); letter-spacing: .5px; line-height: 1;
  }
  .brand-mark { background: var(--red); flex: none; }

  /* front */
  .card-front .brand {
    position: absolute; left: 140px; top: 110px; font-size: 58px;
  }
  .card-front .brand-mark { width: 22px; height: 22px; }
  .front-band {
    position: absolute; left: 0; right: 0; top: 212px; height: 58px;
    background: var(--red);
    display: flex; align-items: center; justify-content: center;
    font-family: "Didact Gothic", sans-serif; font-size: 15px;
    color: var(--white); letter-spacing: .5px;
  }

  /* back */
  .back-strip { position: absolute; left: 0; right: 0; height: 7px; background: var(--red); }
  .back-strip.top { top: 0; }
  .back-strip.bottom { bottom: 0; }
  .card-back .brand {
    position: absolute; left: 34px; top: 150px; font-size: 38px;
  }
  .card-back .brand-mark { width: 15px; height: 15px; }
  .contact {
    position: absolute; left: 318px; top: 84px;
    font-family: "Didact Gothic", sans-serif; color: var(--ink);
  }
  .contact-name {
    font-family: "Poppins", sans-serif; font-weight: 600; font-size: 17px; color: var(--ink);
  }
  .contact-role { font-size: 13px; color: var(--red); margin-top: 2px; }
  .contact-rule { width: 42px; height: 1px; background: var(--ink); margin: 10px 0 12px; }
  .contact-list { list-style: none; }
  .contact-list li {
    display: flex; align-items: center; gap: 10px;
    font-size: 13px; margin-bottom: 9px;
  }
  .contact-list svg { width: 13px; height: 13px; flex: none; }
</style>
</head>
<body>
<main class="canvas">
  <section class="card card-front">
    <div class="brand"><span class="brand-mark"></span>Quorvela</div>
    <div class="front-band">www.quorvela.com.au</div>
  </section>

  <section class="card card-back">
    <div class="back-strip top"></div>
    <div class="brand"><span class="brand-mark"></span>Quorvela</div>
    <div class="contact">
      <p class="contact-name">Danielle Forsk</p>
      <p class="contact-role">Licensee / Director</p>
      <div class="contact-rule"></div>
      <ul class="contact-list">
        <li>
          <svg viewBox="0 0 16 16" aria-hidden="true"><path fill="#ec1f27" d="M2 6c0-2 2.5-3 6-3s6 1 6 3v1h-3V5.5H5V7H2zM4 8h8l2 5H2z"/><circle cx="8" cy="10.5" r="1.5" fill="#fff"/></svg>
          0428 519 064
        </li>
        <li>
          <svg viewBox="0 0 16 16" aria-hidden="true"><rect x="1.5" y="3.5" width="13" height="9" fill="none" stroke="#ec1f27" stroke-width="1.5"/><path d="M1.5 3.5L8 9l6.5-5.5" fill="none" stroke="#ec1f27" stroke-width="1.5"/></svg>
          danielle@quorvela.com.au
        </li>
        <li>
          <svg viewBox="0 0 16 16" aria-hidden="true"><circle cx="8" cy="8" r="6.3" fill="none" stroke="#ec1f27" stroke-width="1.5"/><ellipse cx="8" cy="8" rx="2.6" ry="6.3" fill="none" stroke="#ec1f27" stroke-width="1.2"/><path d="M1.7 8h12.6" stroke="#ec1f27" stroke-width="1.2"/></svg>
          www.quorvela.com.au
        </li>
      </ul>
    </div>
    <div class="back-strip bottom"></div>
  </section>
</main>
</body>
</html>
```